Epoxy Flooring Contractor business card

We need a business card to promote a new addition to our business. We now offer Epoxy Flooring. We would like for the business card to include the images attached. One is our logo, the other is a sample of metallic epoxy flooring, we would like to incorporate that somewhere into the design. I was thinking an icon of a man pushing a concrete grinder and have the color set to the metallic epoxy color. I found a business card sample on this website, I will attach it. It has the icon that we are looking for, or something similar.
Our company name is Brightmore Coatings LLC
Our owners name is Dana Pellow
Phone is 561-847-2916
website is www.brightmore-coatingsllc.com
please let me know if you need any other info

Contact Information for Business Card

Brightmore Coatings LLC
Dana Pellow, owner
Phone: 561-847-2916
Address: P.O Box 8146 Lake Worth, FL 33471
www.Brightmore-CoatingsLLC.com
BrightmoreCoatingsLLC@mailvista.net
Include logo attached
It must include a Clip art of man with concrete grinder
Must include metallic epoxy design attached
Must include the following text
Residential Garage Flooring
Epoxy Countertops
Commercial Epoxy Flooring
Restaurant Flooring
Warehouse Flooring
Licensed & Insured
Free Estimates

Colors

Designer to choose colors to be used in the design.

Requirements
Must have
• Include logo attached
• It must include a Clip art of man with concrete grinder
• Must include metallic epoxy design attached
• Must include the following text
• Garage Epoxy Flooring
• Residential Epoxy Flooring
• Concrete Floor Crack Repairs
• Concrete Floor Grinding
• Commercial & Warehouse Epoxy Flooring
• Restaurant Epoxy Flooring
• Epoxy Countertops
• Non Slip Epoxy Pool Decks
• Textured Finishes, Flakes, Granite Coat, Metallic & Quartz
• FREE ESTIMATES • LICENSED & INSURED

```html
<!DOCTYPE html>
<html lang="en">
<head>
<meta charset="utf-8">
<title>Brightmore Coatings LLC – Business Card</title>
<link href="https://fonts.googleapis.com/css2?family=Montserrat:wght@400;500&family=Roboto+Condensed:wght@400;500;700&display=swap" rel="stylesheet">
<style>
  :root {
    --page: #e7e4df;
    --paper: #f5f5f3;
    --slate: #2b2d30;
    --slate-deep: #1f2022;
    --slate-light: #3d4044;
    --brand-blue: #4f83b2;
    --sky-blue: #8db5d8;
    --pale-blue: #b9d2e8;
    --text-light: #f1f3f5;
    --logo-grey: #6f7a86;
  }
  * { box-sizing: border-box; margin: 0; padding: 0; }
  html, body { width: 1200px; height: 780px; overflow: hidden; }
  body {
    background: var(--page);
    font-family: "Roboto Condensed", Arial, sans-serif;
    position: relative;
  }
  .card {
    position: absolute;
    width: 540px;
    height: 309px;
    border-radius: 14px;
    overflow: hidden;
    box-shadow: 0 6px 18px rgba(0,0,0,.18);
  }
  .card--front { left: 40px; top: 235px; background: var(--paper); }
  .card--back  { left: 620px; top: 235px; }

  .marble {
    position: absolute;
    background:
      radial-gradient(ellipse at 30% 40%, var(--slate-light) 0%, transparent 55%),
      radial-gradient(ellipse at 75% 70%, #34373b 0%, transparent 50%),
      linear-gradient(135deg, var(--slate) 0%, var(--slate-deep) 100%);
  }

  /* Front */
  .front-logo {
    position: absolute; left: 70px; top: 32px;
    display: flex; align-items: center; gap: 16px;
  }
  .front-logo__dot {
    width: 58px; height: 58px; border-radius: 50%;
    background: var(--brand-blue);
  }
  .brand-name {
    font-family: "Montserrat", Arial, sans-serif;
    font-weight: 400;
    color: var(--logo-grey);
    letter-spacing: 3px;
    line-height: 1.05;
  }
  .front-logo .brand-name { font-size: 30px; }

  .name-band {
    position: absolute; left: 0; top: 135px; width: 100%; height: 30px;
    background: var(--brand-blue);
    color: var(--text-light);
    display: flex; align-items: center; padding-left: 22px;
    font-size: 17px; font-weight: 500; letter-spacing: .5px;
  }
  .name-band .role { font-size: 13px; font-weight: 400; margin-left: 6px; }
  .front-dark { left: 0; top: 165px; width: 100%; height: 144px; }

  .contact-list {
    position: absolute; left: 22px; bottom: 18px;
    list-style: none; color: var(--text-light); font-size: 15px;
  }
  .contact-list li { display: flex; align-items: center; gap: 9px; margin-top: 5px; }
  .contact-icon {
    width: 18px; height: 18px; border-radius: 50%;
    background: var(--sky-blue);
    display: flex; align-items: center; justify-content: center;
    flex-shrink: 0;
  }
  .address {
    position: absolute; right: 24px; top: 182px;
    color: var(--text-light); font-size: 15px; line-height: 1.3; text-align: right;
  }

  /* Back */
  .back-dark { inset: 0; }
  .service-list {
    position: absolute; left: 26px; top: 20px;
    list-style: none; color: var(--text-light);
    font-size: 14.5px; line-height: 22px;
  }
  .service-list li { display: flex; align-items: center; gap: 10px; }
  .service-list li::before {
    content: ""; width: 6px; height: 6px; border-radius: 50%;
    background: var(--sky-blue); flex-shrink: 0;
  }
  .back-logo {
    position: absolute; right: 26px; top: 60px;
    display: flex; align-items: center; gap: 12px;
  }
  .back-logo__dot { width: 44px; height: 44px; border-radius: 50%; background: var(--brand-blue); }
  .back-logo .brand-name { font-size: 22px; color: var(--sky-blue); }

  .promise-band {
    position: absolute; left: 0; top: 262px; width: 100%; height: 26px;
    background: var(--pale-blue);
    color: var(--slate); font-weight: 700; font-size: 13.5px; letter-spacing: 1px;
    display: flex; align-items: center; padding-left: 26px;
  }
  .grinder-art {
    position: absolute; left: 300px; top: 150px; width: 190px; height: 150px;
    border-radius: 10px;
    background: linear-gradient(160deg, var(--sky-blue) 0%, var(--brand-blue) 100%);
  }
</style>
</head>
<body>

  <section class="card card--front" aria-label="Business card front">
    <div class="front-logo">
      <span class="front-logo__dot"></span>
      <div class="brand-name">Brightmore<br>Coatings</div>
    </div>

    <div class="name-band">DANA PELLOW&nbsp;|<span class="role">Owner</span></div>
    <div class="marble front-dark"></div>

    <address class="address" style="font-style:normal">P.O Box 8146<br>Lake Worth<br>FL 33471</address>

    <ul class="contact-list">
      <li>
        <span class="contact-icon">
          <svg width="10" height="10" viewBox="0 0 24 24"><path fill="#2b2d30" d="M6.6 10.8a15.1 15.1 0 0 0 6.6 6.6l2.2-2.2a1 1 0 0 1 1-.25 11.4 11.4 0 0 0 3.6.57 1 1 0 0 1 1 1V20a1 1 0 0 1-1 1A17 17 0 0 1 3 4a1 1 0 0 1 1-1h3.5a1 1 0 0 1 1 1c0 1.25.2 2.45.57 3.57a1 1 0 0 1-.25 1z"/></svg>
        </span>561-847-2916
      </li>
      <li>
        <span class="contact-icon">
          <svg width="10" height="10" viewBox="0 0 24 24"><rect x="2" y="5" width="20" height="14" rx="2" fill="#2b2d30"/><path d="M3 6l9 7 9-7" stroke="#8db5d8" stroke-width="2" fill="none"/></svg>
        </span>BrightmoreCoatingsLLC@mailvista.net
      </li>
      <li>
        <span class="contact-icon">
          <svg width="11" height="11" viewBox="0 0 24 24" fill="none" stroke="#2b2d30" stroke-width="2"><circle cx="12" cy="12" r="9"/><path d="M3 12h18M12 3c3 3 3 15 0 18M12 3c-3 3-3 15 0 18"/></svg>
        </span>www.Brightmore-CoatingsLLC.com
      </li>
    </ul>
  </section>

  <section class="card card--back" aria-label="Business card back">
    <div class="marble back-dark"></div>

    <ul class="service-list">
      <li>Garage Epoxy Flooring</li>
      <li>Residential Epoxy Flooring</li>
      <li>Concrete Floor Crack Repairs</li>
      <li>Concrete Floor Grinding</li>
      <li>Commercial &amp; Warehouse Epoxy Flooring</li>
      <li>Restaurant Epoxy Flooring</li>
      <li>Epoxy Countertops</li>
      <li>Non Slip Epoxy Pool Decks</li>
      <li>Textured Finishes, Flakes,</li>
      <li>Granite Coat, Metallic &amp; Quartz</li>
    </ul>

    <div class="back-logo">
      <span class="back-logo__dot"></span>
      <div class="brand-name">Brightmore<br>Coatings</div>
    </div>

    <div class="promise-band">FREE ESTIMATES • LICENSED &amp; INSURED</div>
    <div class="grinder-art" role="img" aria-label="Clip art of a worker in a cap giving a thumbs up beside a concrete floor grinder, in metallic blue tones"></div>
  </section>

</body>
</html>
```